Infographic Customizable and DISC Proof

Design of an infographic used to assist candidates to get an overview on the steps they need to take in order to get the candidate in the best possible position to a new step in their career.

Attached is an outline of the text that needs to be converted to an Infographic.

The infographics will be used predominantly as an attachment in the email from the recruiter to the candidate.

Based on the DISC profile of the candidate we require 2 different designs; 1 designed for yellow disc profiles, stylish, beautifull, with the use of our brand color scheme. And one more factual for example for a blue disc profile with far less or no use of colour and a more sleek clean design.

It is important to take into consideration with your design and format you deliver that we want to be able to change some of the content on the infographics after your delivery completely by ourselves for the following use cases:

1. processes differ per client, hence we must be able to add or remove a step and be able to change the title and body of the steps in order to create an infographic for a different client of ours.
2. We would like to be able to change contact details and the profile picture of the recruiter. Example of a profile picture we would want to use is similar to the profile picture of a workvista profile but then without the background. I attached it as an example for your reference.

It's important to take into consideration that we would need to be able to make such changes by ourselves without the need to become a savvy user of programs such as paint or adobe. The person that would need to be able to make the change is a recruiter, a typical office worker. Please let us know how we would be enabled to do this when you completed the design.

```html
<!DOCTYPE html>
<html lang="nl">
<head>
<meta charset="utf-8">
<title>In 4 stappen optimaal voor het voetlicht</title>
<link rel="stylesheet" href="https://fonts.googleapis.com/css2?family=Poppins:wght@400;600;700;800&family=Oswald:wght@700&display=swap">
<style>
  :root{
    --blue:#0d5aa3;
    --blue-dark:#0a4a88;
    --orange:#f7941d;
    --orange-deep:#f26522;
    --ink:#1b1b1f;
    --text:#2b2f38;
    --white:#ffffff;
    --paper:#fbfbfd;
  }
  *{margin:0;padding:0;box-sizing:border-box}
  html,body{width:800px;height:1200px;overflow:hidden;background:var(--white)}
  body{font-family:"Poppins",sans-serif;color:var(--text)}
  .poster{position:relative;width:800px;height:1200px;background:var(--white);overflow:hidden}

  .brand{position:absolute;left:0;width:800px;top:40px;text-align:center}
  .brand-square{display:block;margin:0 auto;width:60px;height:60px;background:var(--blue)}
  .brand-name{display:block;margin-top:10px;font-weight:600;font-size:34px;letter-spacing:1px;color:var(--blue);line-height:1}

  .headline{position:absolute;top:164px;left:0;width:800px;text-align:center;font-weight:800;line-height:1}
  .headline .line-1{display:block;font-size:47px;color:var(--blue);letter-spacing:-.5px}
  .headline .line-2{display:block;font-size:47px;color:var(--orange);margin-top:4px;letter-spacing:-.5px}

  .step{position:absolute;left:59px;width:696px;height:147px}
  .step-body{position:absolute;top:0;height:147px;background:var(--paper);box-shadow:0 10px 14px -8px rgba(30,40,60,.28)}
  .step-tab{position:absolute;top:0;width:134px;height:147px;color:var(--white);text-align:center}
  .step-tab.blue{left:0;border-radius:56px 0 0 56px;background:linear-gradient(160deg,var(--blue),var(--blue-dark))}
  .step-tab.orange{right:0;width:146px;border-radius:0 56px 56px 0;background:linear-gradient(160deg,var(--orange),var(--orange-deep))}
  .step-label{display:block;margin-top:18px;font-weight:800;font-size:26px;line-height:1}
  .step-icon{display:block;margin:14px auto 0;width:56px;height:60px}
  .step.left .step-body{left:134px;right:16px}
  .step.right .step-body{left:0;right:146px}

  .step-title{position:absolute;font-weight:700;font-size:21px;color:var(--ink);line-height:1;white-space:nowrap}
  .checklist{position:absolute;list-style:none;font-size:12.6px;line-height:16px}
  .checklist li{position:relative;padding-left:20px}
  .checklist li svg{position:absolute;left:0;top:2px;width:12px;height:12px}

  .extra{position:absolute;left:59px;top:887px;width:680px;height:146px}
  .extra-curve{position:absolute;left:0;top:0;width:120px;height:146px;border-radius:58px 0 0 58px;background:linear-gradient(160deg,var(--blue),var(--blue-dark))}
  .extra-body{position:absolute;left:24px;right:0;top:0;height:146px;background:var(--paper);border-radius:46px 0 0 46px;box-shadow:0 10px 14px -8px rgba(30,40,60,.28)}

  .footer{position:absolute;left:0;top:1062px;width:800px;height:138px;background:var(--blue-dark)}
  .footer-bump{position:absolute;left:316px;top:1050px;width:104px;height:104px;border-radius:50%;background:var(--blue-dark)}
  .tagline{position:absolute;left:59px;top:1078px;font-family:"Oswald",sans-serif;font-weight:700;font-size:40px;line-height:40px;letter-spacing:-.5px}
  .tagline .accent{display:block;color:var(--orange)}
  .tagline .plain{display:block;color:var(--white)}
  .recruiter-photo{position:absolute;left:318px;top:1066px;width:100px;height:100px;border-radius:50%;background:radial-gradient(circle at 50% 40%,#8c8f94,#4b4f56)}
  .recruiter{position:absolute;left:445px;top:1070px;color:var(--white)}
  .recruiter-name{font-weight:800;font-size:25px;color:var(--orange);line-height:1}
  .recruiter-role{font-size:13px;font-weight:400;margin-top:4px;line-height:1}
  .contact{display:flex;align-items:center;font-weight:700;font-size:17px;line-height:1;margin-top:9px}
  .contact svg{width:15px;height:15px;margin-right:12px;flex:none}
  .contact + .contact{margin-top:5px}
</style>
</head>
<body>
<svg width="0" height="0" style="position:absolute">
  <defs>
    <symbol id="check-blue" viewBox="0 0 12 12"><rect x="1" y="2" width="9" height="9" rx="1.5" fill="none" stroke="#0d5aa3" stroke-width="1.3"/><path d="M3.2 6.3l2.2 2.2L11 2.6" fill="none" stroke="#0d5aa3" stroke-width="1.6" stroke-linecap="round" stroke-linejoin="round"/></symbol>
    <symbol id="check-orange" viewBox="0 0 12 12"><rect x="1" y="2" width="9" height="9" rx="1.5" fill="none" stroke="#f7941d" stroke-width="1.3"/><path d="M3.2 6.3l2.2 2.2L11 2.6" fill="none" stroke="#f7941d" stroke-width="1.6" stroke-linecap="round" stroke-linejoin="round"/></symbol>
  </defs>
</svg>

<main class="poster">
  <header class="brand">
    <span class="brand-square"></span>
    <span class="brand-name">VELDMARK</span>
  </header>

  <h1 class="headline">
    <span class="line-1">IN 4 STAPPEN OPTIMAAL</span>
    <span class="line-2">VOOR HET VOETLICHT</span>
  </h1>

  <!-- Stap 1 -->
  <section class="step left" style="top:301px">
    <div class="step-body"></div>
    <div class="step-tab blue">
      <span class="step-label">STAP 1</span>
      <svg class="step-icon" viewBox="0 0 56 60" fill="none" stroke="#fff" stroke-width="1.6">
        <rect x="6" y="6" width="44" height="48" rx="2"/><line x1="20" y1="6" x2="20" y2="54"/>
        <circle cx="13" cy="14" r="3.5"/><rect x="9" y="24" width="8" height="4"/><rect x="9" y="32" width="8" height="4"/><rect x="9" y="40" width="8" height="4"/>
        <text x="25" y="17" fill="#fff" stroke="none" font-family="Poppins,sans-serif" font-size="9" font-weight="600">CV</text>
        <line x1="25" y1="24" x2="45" y2="24"/><line x1="25" y1="30" x2="45" y2="30"/><line x1="25" y1="36" x2="45" y2="36"/><line x1="25" y1="42" x2="45" y2="42"/><line x1="25" y1="48" x2="40" y2="48"/>
      </svg>
    </div>
    <h2 class="step-title" style="left:151px;top:15px">CV VOORBEREIDEN</h2>
    <ul class="checklist" style="left:151px;top:47px;width:300px">
      <li><svg><use href="#check-blue"/></svg>Gebruik het bijgevoegde CV-template</li>
      <li><svg><use href="#check-blue"/></svg>Maximaal 7 pagina's A4</li>
      <li><svg><use href="#check-blue"/></svg>Schrijf in het Nederlands</li>
      <li><svg><use href="#check-blue"/></svg>Volg de specifieke datumnotatie [dd-mm-jjjj]</li>
    </ul>
    <ul class="checklist" style="left:473px;top:47px;width:205px">
      <li><svg><use href="#check-blue"/></svg>Vermeld uren per week bij elke functie in het werkverleden</li>
      <li><svg><use href="#check-blue"/></svg>Voeg blokken toe waar nodig</li>
    </ul>
  </section>

  <!-- Stap 2 -->
  <section class="step right" style="top:448px">
    <div class="step-body"></div>
    <div class="step-tab orange">
      <span class="step-label">STAP 2</span>
      <svg class="step-icon" viewBox="0 0 56 60" fill="none" stroke="#fff" stroke-width="1.6">
        <path d="M8 6h28l10 10v38H8z"/><circle cx="27" cy="18" r="7"/><path d="M23.5 18l2.5 2.5 4.5-5"/>
        <path d="M12 32l2 2 3-4M12 40l2 2 3-4M12 48l2 2 3-4"/><line x1="20" y1="33" x2="32" y2="33"/><line x1="20" y1="41" x2="30" y2="41"/><line x1="20" y1="49" x2="34" y2="49"/>
        <path d="M50 22l4 4-16 16-5 1 1-5z"/>
      </svg>
    </div>
    <h2 class="step-title" style="left:15px;top:31px">EISEN EN WENSEN BEARGUMENTEREN</h2>
    <ul class="checklist" style="left:15px;top:67px;width:260px">
      <li><svg><use href="#check-orange"/></svg>Beargumenteer eisen beknopt en herleidbaar</li>
      <li><svg><use href="#check-orange"/></svg>Beargumenteer wensen uitgebreid en kwalitatief</li>
    </ul>
    <ul class="checklist" style="left:291px;top:67px;width:250px">
      <li><svg><use href="#check-orange"/></svg>Geef situatieschetsen en voorbeelden van ervaring</li>
      <li><svg><use href="#check-orange"/></svg>Vermeld het aantal maanden ervaring per gevraagd element</li>
    </ul>
  </section>

  <!-- Stap 3 -->
  <section class="step left" style="top:594px">
    <div class="step-body"></div>
    <div class="step-tab blue">
      <span class="step-label">STAP 3</span>
      <svg class="step-icon" viewBox="0 0 56 60" fill="none" stroke="#fff" stroke-width="1.6">
        <path d="M18 56V46c-5-3-8-8-8-14 0-11 8-19 19-19s18 8 18 18c0 8-4 12-6 15v10"/>
        <circle cx="29" cy="30" r="8"/><path d="M30 25l-3 6h4l-3 5"/><path d="M25 39h8M26 43h6"/>
        <path d="M29 14v-4M40 19l3-3M18 19l-3-3M45 30h4M9 30h4"/>
      </svg>
    </div>
    <h2 class="step-title" style="left:151px;top:31px">MOTIVATIE MET INTRODUCTIE</h2>
    <ul class="checklist" style="left:151px;top:62px;width:245px">
      <li><svg><use href="#check-blue"/></svg>Schrijf een korte, persoonlijke introductie</li>
    </ul>
    <ul class="checklist" style="left:417px;top:62px;width:230px">
      <li><svg><use href="#check-blue"/></svg>Benadruk jouw kracht en motivatie voor de rol en de organisatie</li>
    </ul>
  </section>

  <!-- Stap 4 -->
  <section class="step right" style="top:741px">
    <div class="step-body"></div>
    <div class="step-tab orange">
      <span class="step-label">STAP 4</span>
      <svg class="step-icon" viewBox="0 0 56 60" fill="none" stroke="#fff" stroke-width="1.6">
        <circle cx="10" cy="8" r="3"/><circle cx="48" cy="8" r="3"/><circle cx="6" cy="34" r="3"/><circle cx="50" cy="34" r="3"/>
        <path d="M12.5 10l10 8M45.5 10l-10 8M9 33l10-6M47 33l-10-6"/>
        <circle cx="29" cy="24" r="7"/>
        <path d="M27 58V34a2.5 2.5 0 015 0v10l8 2c2 .5 3 2 3 4l-1 8"/><path d="M27 44l-4-3c-2-1-4 1-3 3l6 10"/>
      </svg>
    </div>
    <h2 class="step-title" style="left:17px;top:23px">CONTROLEER EN VERSTUUR</h2>
    <ul class="checklist" style="left:15px;top:55px;width:270px">
      <li><svg><use href="#check-orange"/></svg>Controleer alle documenten op volledigheid en nauwkeurigheid</li>
      <li><svg><use href="#check-orange"/></svg>Verstuur je CV, beargumentatie en motivatie per e-mail</li>
    </ul>
    <ul class="checklist" style="left:309px;top:55px;width:200px">
      <li><svg><use href="#check-orange"/></svg>Bevestig de financiële aanbieding per e-mail</li>
    </ul>
  </section>

  <!-- Extra ondersteuning -->
  <section class="extra">
    <div class="extra-curve"></div>
    <div class="extra-body"></div>
    <h2 class="step-title" style="left:52px;top:36px">EXTRA ONDERSTEUNING</h2>
    <ul class="checklist" style="left:52px;top:73px;width:300px">
      <li><svg><use href="#check-blue"/></svg>Neem contact op met je toegewezen contactpersoon voor vragen</li>
    </ul>
    <ul class="checklist" style="left:388px;top:73px;width:270px">
      <li><svg><use href="#check-blue"/></svg>Raadpleeg bijgevoegde voorbeeld beargumentatie</li>
    </ul>
  </section>

  <footer>
    <div class="footer"></div>
    <div class="footer-bump"></div>
    <p class="tagline"><span class="accent">AANDACHT</span><span class="plain">VOOR IMPACT</span></p>
    <div class="recruiter-photo" role="img" aria-label="Profielfoto van de recruiter"></div>
    <div class="recruiter">
      <p class="recruiter-name">SANNE VERMEER</p>
      <p class="recruiter-role">RECRUITER</p>
      <p class="contact">
        <svg viewBox="0 0 16 16"><circle cx="8" cy="8" r="8" fill="#f7941d"/><path d="M5.2 4.2l1.6-.4.9 2-1 .8a6 6 0 002.7 2.7l.8-1 2 .9-.4 1.6c-3.6.2-6.9-3-6.6-6.6z" fill="#fff"/></svg>
        010 2345 6789
      </p>
      <p class="contact">
        <svg viewBox="0 0 16 16"><circle cx="8" cy="8" r="8" fill="#f7941d"/><rect x="4" y="5" width="8" height="6" rx="1" fill="#fff"/><path d="M4.3 5.4L8 8.4l3.7-3" fill="none" stroke="#f7941d" stroke-width="1"/></svg>
        contact@sannevermeer.nl
      </p>
    </div>
  </footer>
</main>
</body>
</html>
```